KVT Business Cards

We require business cards for our business. We would like a matte black back to the card, with our logo centred in the middle. The front side of the card is open to design.

Target Market(s)

Clients looking for legal services (professional)

Industry/Entity Type

Legal

Contact Information for Business Card

Boris Telemark
Partner
Mobile: 0438 715 642
Email: boris@kvtlaw.co
Website: www.kvtlaw.co
Level 3, 118 Wexbury Street
Sydney NSW 2000

Font styles to use
Other font styles liked:
• Avenir

Colors
f04a50
ffffff
1b1b1b

Requirements
Must have
• Black back with logo included in the centre of the card.
• Our font is Avenir.

```html
<!DOCTYPE html>
<html lang="en">
<head>
<meta charset="utf-8">
<title>KVT Business Cards</title>
<link rel="stylesheet" href="https://fonts.googleapis.com/css2?family=Nunito+Sans:wght@400;600;700&family=Oswald:wght@500&display=swap">
<style>
  :root {
    --stage: #111111;
    --card: #1b1b1b;
    --card-edge: #262626;
    --silver: #d9d9d9;
    --silver-soft: #a9a9a9;
    --emboss: #121212;
    --emboss-light: #2c2c2c;
    --rule: #4a4a4a;
  }
  * { margin: 0; padding: 0; box-sizing: border-box; }
  html, body {
    width: 1200px; height: 900px; overflow: hidden;
    background: var(--stage);
  }
  .canvas {
    position: relative; width: 1200px; height: 900px;
    background: radial-gradient(ellipse at 50% 45%, #222 0%, var(--stage) 70%);
  }
  .card {
    position: absolute; left: 290px; width: 620px; height: 354px;
    background: linear-gradient(135deg, #1e1e1e 0%, var(--card) 55%, #232323 100%);
    border: 1px solid var(--card-edge);
    box-shadow: 0 18px 40px rgba(0,0,0,.6);
  }
  .card--brand { top: 64px; }
  .card--contact { top: 482px; }

  /* brand side */
  .brand {
    position: absolute; left: 50%; top: 50%; transform: translate(-50%, -50%);
    display: flex; align-items: center; gap: 26px;
  }
  .brand__square { width: 64px; height: 64px; background: #2a2a2a; }
  .brand__name {
    font-family: "Nunito Sans", sans-serif; font-weight: 700;
    font-size: 27px; line-height: 1.05; letter-spacing: 1px;
    color: var(--silver); text-transform: uppercase;
  }

  /* contact side */
  .person {
    position: absolute; left: 60px; top: 118px; text-align: right; width: 250px;
  }
  .person__name {
    font-family: "Oswald", sans-serif; font-weight: 500; font-size: 38px;
    text-transform: uppercase; letter-spacing: .5px; color: var(--emboss);
    text-shadow: 1px 1px 0 var(--emboss-light), -1px -1px 0 #0b0b0b;
  }
  .person__role {
    font-family: "Nunito Sans", sans-serif; font-size: 16px; color: var(--emboss);
    text-shadow: 1px 1px 0 var(--emboss-light);
    margin-top: -2px;
  }
  .divider {
    position: absolute; left: 334px; top: 118px; width: 1px; height: 78px;
    background: var(--rule);
  }
  .contact-list {
    position: absolute; left: 356px; top: 122px; list-style: none;
    font-family: "Nunito Sans", sans-serif; font-size: 18px; color: var(--silver);
  }
  .contact-list li { display: flex; align-items: center; gap: 9px; height: 25px; }
  .contact-list svg { width: 12px; height: 12px; fill: none; stroke: var(--silver-soft); stroke-width: 1.6; }
  .address {
    position: absolute; left: 60px; bottom: 44px;
    font-family: "Nunito Sans", sans-serif; font-size: 17px; color: var(--emboss);
    text-shadow: 1px 1px 0 var(--emboss-light);
  }
</style>
</head>
<body>
<main class="canvas">
  <section class="card card--brand" aria-label="Card back">
    <div class="brand">
      <div class="brand__square"></div>
      <div class="brand__name">Keston<br>Varlow<br>Legal</div>
    </div>
  </section>

  <section class="card card--contact" aria-label="Card front">
    <div class="person">
      <p class="person__name">Boris Telemark</p>
      <p class="person__role">General Manager</p>
    </div>
    <div class="divider"></div>
    <ul class="contact-list">
      <li>
        <svg viewBox="0 0 12 12"><path d="M2.5 1.5 L4.5 1.5 L5 4 L3.8 5 Q5 7.4 7 8.2 L8 7 L10.5 7.5 L10.5 9.5 Q10 10.8 8.5 10.5 Q3 9 1.5 3.5 Q1.2 2 2.5 1.5 Z"/></svg>
        0438 715 642
      </li>
      <li>
        <svg viewBox="0 0 12 12"><rect x="1" y="2.5" width="10" height="7"/><path d="M1 2.5 L6 6.5 L11 2.5"/></svg>
        boris@kvtlaw.co
      </li>
      <li>
        <svg viewBox="0 0 12 12"><circle cx="6" cy="6" r="5"/><path d="M1 6 H11 M6 1 Q3 6 6 11 Q9 6 6 1"/></svg>
        www.kvtlaw.co
      </li>
    </ul>
    <p class="address">Level 3, 118 Wexbury Street</p>
  </section>
</main>
</body>
</html>
```